DL size flyer for Autism Consultancy website

We need a printed flyer DL size ( 210mmx99mm) for our Autism Consultancy website www.brightpathkids.nz which provides therapy for autistic children.
I want the flyer to look consistent with the website’s design. Please feel free to use the colour scheme, fonts, icons or any images from www.brightpathkids.nz.It should be easy to see “Autism” or “Autistic” word from a distance.
Please use either an oversized logo or make “Do you have a verbal and able autistic child?” more prominent.
Please do not convert the text fields to outlines, i.e. I need to be able to edit any text after.The final design should be either in Adobe Illustrator or Adobe Photoshop format.
The Specs for the flyer are
Document Trim Size99 x 210 mm 1169 x 2480 pixels
Full Bleed Size102 x 213 mm 1205 x 2516 pixels
Our Logo https://1drv.ms/u/s!AoH0rRjDY2GYg6QtU-xjoVlmslKp6gPlease
use this photo for the front side https://qzdropbin.io/f/Pw4KcN8rTyH2mXs6BvLd9QeFz1Gj
another one for reverse
https://qzdropbin.io/f/Rk2HsV5nWqJ7tZc3MfXb8LpYd4Ne
Please use the following content:
Do you have a verbal and able autistic child?
We use child-centred, modern and innovative approaches
Teaching autistic children to bond, laugh and play.
We work with schools
We help autistic children to develop social minds
We offer:
• Specialist assessments
• Consultations for parents & schools
• Social learning programmes
• Social-cognitive therapy
We can create an individual learning path, best suited for your child.
Our programmes and interventions include:
• Chatter Quest
• Peer Bright
• Team Puzzles
• Tingle Words
• Pebble Tales
• Pembrook Speech Ladder
• Vorlin Method
• BRIMLE Method
• Tandem Pattern Coaching
contact details on both sides:
www.brightpathkids.nz
info@brightpathkids.nz
(09) 57-318-46

```html
<!DOCTYPE html>
<html lang="en">
<head>
<meta charset="utf-8">
<title>BrightPath Kids – DL Flyer</title>
<link href="https://fonts.googleapis.com/css2?family=Montserrat:wght@600;800&family=Open+Sans:wght@400;600&display=swap" rel="stylesheet">
<style>
  :root{
    --navy:#1d2a5a;
    --navy-deep:#141d45;
    --yellow:#f6c91c;
    --teal:#3cc3c6;
    --white:#ffffff;
    --paper:#f4f4f6;
    --stage:#e7e0d6;
    --ink:#1d2a5a;
  }
  *{box-sizing:border-box;margin:0;padding:0}
  html,body{width:1200px;height:900px;overflow:hidden;background:var(--stage)}
  body{position:relative;font-family:"Open Sans",Arial,sans-serif;color:var(--ink)}
  .flyer{position:absolute;top:30px;width:396px;height:840px;background:var(--white);overflow:hidden;box-shadow:0 6px 18px rgba(0,0,0,.12)}
  .flyer--back{left:180px}
  .flyer--front{left:624px}

  /* shared */
  .photo{position:absolute;left:0;width:100%}
  .notch{position:absolute;left:0;width:100%;display:block}
  .footer{position:absolute;left:0;bottom:0;width:100%;height:78px;background:var(--navy-deep);display:flex;justify-content:space-around;align-items:center;padding:0 10px}
  .contact{display:flex;flex-direction:column;align-items:center;gap:5px;color:var(--white);font-size:10px}
  .contact svg{width:18px;height:18px}

  /* back side */
  .programmes-title{position:absolute;top:0;left:0;width:100%;height:50px;background:var(--navy);color:var(--yellow);font-family:"Montserrat",sans-serif;font-weight:600;font-size:15px;display:flex;align-items:center;justify-content:center}
  .programme{position:absolute;display:flex;flex-direction:column;align-items:center;width:170px}
  .programme-icon{width:40px;height:40px;border-radius:50%;background:var(--white);border:4px solid var(--yellow);display:flex;align-items:center;justify-content:center;margin-bottom:-6px;position:relative;z-index:1}
  .programme-icon--teal{border-color:var(--teal)}
  .programme-icon span{width:12px;height:12px;border-radius:50%;border:2px solid var(--navy)}
  .programme-label{background:var(--navy);color:var(--white);font-family:"Montserrat",sans-serif;font-weight:600;font-size:11.5px;padding:9px 10px;width:100%;text-align:center;line-height:1.15}
  .photo--back{top:430px;height:330px;background:linear-gradient(160deg,#f0d9c0 0%,#d9a27a 35%,#c7453a 55%,#3f8bc9 75%,#e9e3da 100%)}
  .path-band{position:absolute;left:0;top:680px;width:100%;height:80px;background:rgba(29,42,90,.85);color:var(--white);font-size:15px;font-weight:600;line-height:1.3;display:flex;align-items:center;padding:0 22px}

  /* front side */
  .brand{position:absolute;top:22px;left:0;width:100%;display:flex;align-items:center;justify-content:center;gap:10px}
  .brand-mark{width:22px;height:22px;border-radius:50%;background:var(--yellow)}
  .brand-name{font-family:"Montserrat",sans-serif;font-weight:800;font-size:20px;color:var(--navy)}
  .headline{position:absolute;top:70px;left:0;width:100%;text-align:center;font-family:"Montserrat",sans-serif;font-weight:800;font-size:27px;line-height:1.08;color:var(--navy);text-transform:uppercase}
  .headline-accent{color:var(--yellow)}
  .photo--front{top:178px;height:352px;background:linear-gradient(150deg,#f3ede4 0%,#f2d35a 30%,#d9a47f 50%,#6fa9d6 72%,#e8e1d6 100%)}
  .approach-band{position:absolute;left:0;top:440px;width:100%;height:90px;background:rgba(29,42,90,.85);color:var(--white);font-size:11.5px;line-height:1.55;padding:12px 22px}
  .approach-band li{list-style:none;padding-left:12px;position:relative}
  .approach-band li::before{content:"";position:absolute;left:0;top:7px;width:4px;height:4px;border-radius:50%;background:var(--white)}
  .offer-title{position:absolute;top:530px;left:0;width:100%;height:34px;background:var(--navy);color:var(--yellow);font-family:"Montserrat",sans-serif;font-weight:800;font-size:17px;padding:7px 22px}
  .offer-list{position:absolute;top:578px;left:22px;right:16px;list-style:none}
  .offer-item{display:flex;align-items:center;gap:10px;font-size:16px;color:var(--navy);margin-bottom:14px}
  .offer-num{flex:none;width:30px;height:22px;background:var(--yellow);color:var(--white);font-size:10px;font-weight:600;display:flex;align-items:center;justify-content:center;clip-path:polygon(25% 0,100% 0,100% 100%,25% 100%,0 50%)}
</style>
</head>
<body>

<!-- Reverse side -->
<section class="flyer flyer--back">
  <h2 class="programmes-title">Our programmes and interventions include:</h2>

  <div class="programme" style="left:22px;top:80px"><div class="programme-icon"><span></span></div><div class="programme-label">Chatter Quest</div></div>
  <div class="programme" style="left:204px;top:60px"><div class="programme-icon programme-icon--teal"><span></span></div><div class="programme-label">Team Puzzles</div></div>
  <div class="programme" style="left:22px;top:160px"><div class="programme-icon programme-icon--teal"><span></span></div><div class="programme-label">Peer Bright</div></div>
  <div class="programme" style="left:204px;top:140px"><div class="programme-icon"><span></span></div><div class="programme-label">Pebble Tales</div></div>
  <div class="programme" style="left:22px;top:240px"><div class="programme-icon"><span></span></div><div class="programme-label">Tingle Words</div></div>
  <div class="programme" style="left:204px;top:220px"><div class="programme-icon programme-icon--teal"><span></span></div><div class="programme-label">Pembrook Speech Ladder</div></div>
  <div class="programme" style="left:22px;top:320px"><div class="programme-icon programme-icon--teal"><span></span></div><div class="programme-label">Vorlin Method</div></div>
  <div class="programme" style="left:204px;top:300px"><div class="programme-icon"><span></span></div><div class="programme-label">BRIMLE Method</div></div>
  <div class="programme" style="left:110px;top:370px;width:240px"><div class="programme-icon"><span></span></div><div class="programme-label">Tandem Pattern Coaching</div></div>

  <div class="photo photo--back" role="img" aria-label="Photo of a young child lying on the floor playing with colourful toys"></div>
  <svg class="notch" style="top:430px" width="396" height="40" viewBox="0 0 396 40"><polygon points="0,0 396,0 396,10 160,10 120,40 80,10 0,10" fill="#ffffff"/></svg>
  <p class="path-band">We can create an individual learning path, best suited for your child.</p>

  <footer class="footer">
    <div class="contact"><svg viewBox="0 0 20 20" fill="none" stroke="#fff" stroke-width="1.5"><circle cx="10" cy="10" r="8"/><ellipse cx="10" cy="10" rx="3.5" ry="8"/><line x1="2" y1="10" x2="18" y2="10"/></svg>www.brightpathkids.nz</div>
    <div class="contact"><svg viewBox="0 0 20 20"><rect x="2" y="5" width="16" height="11" fill="#fff"/><polyline points="2,5 10,11 18,5" fill="none" stroke="#141d45" stroke-width="1.5"/></svg>info@brightpathkids.nz</div>
  </footer>
</section>

<!-- Front side -->
<section class="flyer flyer--front">
  <div class="brand"><span class="brand-mark"></span><span class="brand-name">BrightPath Kids</span></div>
  <h1 class="headline">Do you have a<br>verbal and able<br><span class="headline-accent">autistic child?</span></h1>

  <div class="photo photo--front" role="img" aria-label="Photo of a smiling boy holding a teddy bear with a therapist"></div>
  <svg class="notch" style="top:178px" width="396" height="50" viewBox="0 0 396 50"><polygon points="0,0 396,0 396,4 200,4 140,50 100,20 0,20" fill="#ffffff"/></svg>

  <ul class="approach-band">
    <li>We use child-centred, modern and innovative approaches</li>
    <li>Teaching autistic children to bond, laugh and play</li>
    <li>We work with schools</li>
    <li>We help autistic children to develop social minds</li>
  </ul>

  <h2 class="offer-title">WE OFFER:</h2>
  <ol class="offer-list">
    <li class="offer-item"><span class="offer-num">01</span>Consultations for parents &amp; schools</li>
    <li class="offer-item"><span class="offer-num">02</span>Social learning programmes</li>
    <li class="offer-item"><span class="offer-num">03</span>Social-cognitive therapy</li>
    <li class="offer-item"><span class="offer-num">04</span>Specialist assessments</li>
  </ol>

  <footer class="footer">
    <div class="contact"><svg viewBox="0 0 20 20" fill="none" stroke="#fff" stroke-width="1.5"><circle cx="10" cy="10" r="8"/><ellipse cx="10" cy="10" rx="3.5" ry="8"/><line x1="2" y1="10" x2="18" y2="10"/></svg>www.brightpathkids.nz</div>
    <div class="contact"><svg viewBox="0 0 20 20"><rect x="2" y="5" width="16" height="11" fill="#fff"/><polyline points="2,5 10,11 18,5" fill="none" stroke="#141d45" stroke-width="1.5"/></svg>info@brightpathkids.nz</div>
    <div class="contact"><svg viewBox="0 0 20 20"><path d="M5 2l3 4-2 2c1 2 3 4 5 5l2-2 4 3-2 3C9 17 3 11 2 4z" fill="#fff"/></svg>(09) 57-318-46</div>
  </footer>
</section>

</body>
</html>
```